Rinsely Surface Cleaning - Business Card Design

Use company logo and design a new business card. We are looking for a front and back design. The back should be a dark purple background. We want the back to show cartoon-like soap bubbles chasing mildew cartoon shaped figures. This gives the idea that Rinsely Surface Cleaning provides exterior washing services that work. No mildew stands a chance when Rinsely Surface Cleaning shows up to work. The mildew cartoon images should be green in color, have eyes, and look scared of the bubbles. The bubbles should be light blue in color and have eyes that looked excited to be there.
We will advertise on Chatterly and Pixalonia. These Chatterly and Pixalonia icons should be somewhere on the card.

```html
<!DOCTYPE html>
<html lang="en">
<head>
<meta charset="utf-8">
<title>Rinsely Surface Cleaning – Business Card</title>
<link href="https://fonts.googleapis.com/css2?family=Lexend:wght@300;400;600;700&display=swap" rel="stylesheet">
<style>
  :root {
    --backdrop: #9775ea;
    --ink: #3b2360;
    --ink-soft: #4a3a66;
    --card-light: #eceef1;
    --card-glow: #ffffff;
    --card-dark: #3b2360;
    --cloud-dark: #46336b;
    --cloud-light: #f6f7f8;
    --puddle: #56508d;
    --bubble-blue: #27a6e0;
    --mildew-green: #8cc63f;
    --white: #ffffff;
  }
  * { box-sizing: border-box; margin: 0; padding: 0; }
  html, body { width: 1200px; height: 1200px; overflow: hidden; }
  body {
    background: var(--backdrop);
    font-family: "Lexend", sans-serif;
    color: var(--ink);
    position: relative;
  }
  .card {
    position: absolute;
    left: 235px;
    width: 729px;
    height: 443px;
    border-radius: 28px;
    overflow: hidden;
    box-shadow: 0 16px 10px -6px rgba(80, 50, 150, 0.45);
  }
  .card-front {
    top: 127px;
    background: radial-gradient(ellipse 55% 60% at 50% 50%, var(--card-glow), var(--card-light));
  }
  .card-back {
    top: 604px;
    background: var(--card-dark);
  }
  .clouds { position: absolute; inset: 0; width: 100%; height: 100%; }

  .brand-name {
    position: absolute;
    left: 48px;
    top: 178px;
    width: 290px;
    display: flex;
    align-items: center;
    gap: 10px;
    font-weight: 700;
    font-size: 26px;
    line-height: 1.1;
    color: var(--ink);
  }
  .brand-dot {
    flex: none;
    width: 30px; height: 30px;
    border-radius: 50%;
    background: var(--ink);
  }
  .divider {
    position: absolute;
    left: 364px; top: 107px;
    width: 1.5px; height: 229px;
    background: var(--ink-soft);
  }
  .holder { position: absolute; left: 416px; top: 100px; }
  .holder-name { font-size: 30px; line-height: 1; letter-spacing: 0.5px; font-weight: 300; }
  .holder-name strong { font-weight: 700; }
  .holder-role { margin: 8px 0 0 6px; font-size: 16px; font-weight: 300; letter-spacing: 0.5px; color: var(--ink-soft); }

  .contact-list { position: absolute; left: 423px; top: 181px; list-style: none; }
  .contact-item {
    display: flex; align-items: center; gap: 16px;
    font-size: 16.5px; font-weight: 300; color: var(--ink);
    margin-bottom: 13px; line-height: 1.25;
  }
  .contact-item svg { flex: none; width: 18px; height: 18px; fill: var(--ink); }
  .contact-item.address { align-items: center; }

  .social-row { position: absolute; top: 387px; left: 162px; display: flex; gap: 72px; }
  .social-handle { display: flex; align-items: center; gap: 8px; font-size: 17px; font-weight: 300; }
  .social-dot { width: 20px; height: 20px; border-radius: 50%; background: var(--ink); }

  .brand-name-light {
    position: absolute; left: 30px; top: 36px;
    display: flex; align-items: center; gap: 7px;
    font-weight: 700; font-size: 17px; line-height: 1.1;
    color: var(--white); width: 170px;
  }
  .brand-name-light .brand-dot { width: 20px; height: 20px; background: var(--white); }

  .scene-art {
    position: absolute;
    left: 156px; top: 86px;
    width: 416px; height: 266px;
    border-radius: 40% 40% 30% 30% / 45% 45% 25% 25%;
    background:
      radial-gradient(circle at 72% 40%, var(--bubble-blue) 0 26%, transparent 27%),
      radial-gradient(circle at 22% 60%, var(--mildew-green) 0 15%, transparent 16%),
      linear-gradient(180deg, rgba(86,80,141,0) 40%, var(--puddle) 80%);
  }
</style>
</head>
<body>

<section class="card card-front" aria-label="Business card front">
  <svg class="clouds" viewBox="0 0 729 443" aria-hidden="true">
    <g fill="var(--cloud-light)">
      <circle cx="40" cy="20" r="110"/>
      <circle cx="160" cy="-10" r="90"/>
      <circle cx="450" cy="-40" r="80"/>
      <circle cx="620" cy="10" r="80"/>
      <circle cx="740" cy="70" r="90"/>
      <circle cx="30" cy="420" r="110"/>
      <circle cx="160" cy="470" r="90"/>
      <circle cx="700" cy="430" r="120"/>
      <circle cx="205" cy="96" r="22"/>
      <circle cx="205" cy="348" r="22"/>
      <circle cx="585" cy="96" r="13"/>
      <circle cx="585" cy="348" r="13"/>
    </g>
  </svg>

  <div class="brand-name"><span class="brand-dot"></span>Rinsely Surface Cleaning</div>

  <div class="divider"></div>

  <div class="holder">
    <h1 class="holder-name"><strong>YOUR</strong> NAME</h1>
    <p class="holder-role">POSITION</p>
  </div>

  <ul class="contact-list">
    <li class="contact-item">
      <svg viewBox="0 0 24 24"><path d="M6.6 10.8a15.1 15.1 0 0 0 6.6 6.6l2.2-2.2c.3-.3.7-.4 1-.2 1.1.4 2.3.6 3.6.6.6 0 1 .4 1 1V20c0 .6-.4 1-1 1A17 17 0 0 1 3 4c0-.6.4-1 1-1h3.5c.6 0 1 .4 1 1 0 1.3.2 2.5.6 3.6.1.3 0 .7-.2 1z"/></svg>
      +123456789
    </li>
    <li class="contact-item">
      <svg viewBox="0 0 24 24"><path d="M3 5h18v14H3zm2 2v.5l7 5 7-5V7z"/></svg>
      username@email.com
    </li>
    <li class="contact-item address">
      <svg viewBox="0 0 24 24"><path d="M12 2a7 7 0 0 0-7 7c0 5.2 7 13 7 13s7-7.8 7-13a7 7 0 0 0-7-7zm0 9.5A2.5 2.5 0 1 1 12 6.5a2.5 2.5 0 0 1 0 5z"/></svg>
      <span>Street Address Here<br>Nowhere, 4444</span>
    </li>
    <li class="contact-item">
      <svg viewBox="0 0 24 24" fill="none" stroke="var(--ink)" stroke-width="1.8"><circle cx="12" cy="12" r="9"/><path d="M3 12h18M12 3c3 3 3 15 0 18M12 3c-3 3-3 15 0 18M5 7.5h14M5 16.5h14"/></svg>
      www.yourwebsite.com
    </li>
  </ul>

  <div class="social-row">
    <span class="social-handle"><span class="social-dot"></span>Your Pixalonia</span>
    <span class="social-handle"><span class="social-dot"></span>Your Chatterly</span>
  </div>
</section>

<section class="card card-back" aria-label="Business card back">
  <svg class="clouds" viewBox="0 0 729 443" aria-hidden="true">
    <g fill="var(--cloud-dark)">
      <circle cx="40" cy="40" r="110"/>
      <circle cx="200" cy="-20" r="90"/>
      <circle cx="440" cy="-40" r="80"/>
      <circle cx="620" cy="10" r="80"/>
      <circle cx="740" cy="80" r="90"/>
      <circle cx="20" cy="470" r="140"/>
      <circle cx="230" cy="490" r="90"/>
      <circle cx="470" cy="500" r="100"/>
      <circle cx="720" cy="460" r="130"/>
      <circle cx="208" cy="96" r="22"/>
      <circle cx="149" cy="357" r="18"/>
      <circle cx="585" cy="96" r="13"/>
      <circle cx="490" cy="366" r="13"/>
    </g>
  </svg>

  <div class="brand-name-light"><span class="brand-dot"></span>Rinsely Surface Cleaning</div>

  <div class="scene-art" role="img" aria-label="Cartoon illustration: excited light blue soap bubbles chasing a scared green mildew figure across a puddle"></div>
</section>

</body>
</html>
```